" Não vendemos nossos serviços "no varejo". Somos chamados a participar de projetos de investimento no Brasil ainda na fase de concepção, sob acordo de confidencialidade, buscando alimentar a modelagem financeira com os inputs tributários que frequentemente são cruciais na definição de viabilidade do projeto. Também somos chamados por nossos clientes para avaliar ou alocar contratualmente riscos decorrentes de contingências fiscais, especialmente em fusões e aquisições de empresas. E, ainda, patrocinar defesas ou pleitos em processos administrativos ou judiciais, sempre tendo como parte adversária o fisco (federal, estadual ou municipal). Atuamos em um ambiente profissional onde ética, compliance, qualidade e comprometimento são premissas. O propósito de nossa empresa é a criação de valor de modo sustentável, em questões fiscais, para negócios empreendidos no Brasil. "

```html
<!DOCTYPE html>
<html lang="pt-BR">
<head>
<meta charset="UTF-8">
<title>Ferraz Lacerda Moura Advogados – Papel timbrado</title>
<link href="https://fonts.googleapis.com/css2?family=Raleway:wght@300;400;600&display=swap" rel="stylesheet">
<style>
  :root {
    --backdrop: #e9ebef;
    --paper: #ffffff;
    --brand-light: #7c94c6;
    --brand-navy: #1f2f5c;
    --band: #5a7cb8;
    --ink-soft: #6d7688;
    --ghost: #eef0f3;
  }
  * { margin: 0; padding: 0; box-sizing: border-box; }
  html, body {
    width: 1200px; height: 1200px; overflow: hidden;
    background: var(--backdrop);
    font-family: "Raleway", sans-serif;
  }
  .letterhead {
    position: absolute; left: 211px; top: 50px;
    width: 778px; height: 1100px;
    background: var(--paper);
    box-shadow: 0 6px 24px rgba(30, 40, 70, 0.12);
    overflow: hidden;
  }
  .masthead {
    position: absolute; left: 56px; top: 40px;
    display: flex; align-items: flex-start; gap: 22px;
  }
  .firm-name {
    color: var(--brand-light);
    font-weight: 300; font-size: 19px; line-height: 21px;
    letter-spacing: 1.5px; text-transform: uppercase;
  }
  .firm-name span { display: block; }
  .firm-name span:nth-child(2) { padding-left: 8px; }
  .firm-name span:nth-child(3) { padding-left: 0; }
  .brand-mark {
    display: flex; align-items: center; gap: 8px;
    margin-top: 10px;
    color: var(--brand-navy);
    font-weight: 600; font-size: 30px; letter-spacing: 3px;
  }
  .brand-mark i {
    display: block; width: 12px; height: 12px;
    background: var(--brand-navy);
  }
  .ghost-name {
    position: absolute; left: 0; right: 0; top: 470px;
    text-align: center;
    color: var(--ghost);
    font-weight: 600; font-size: 140px; letter-spacing: 18px;
  }
  .contact {
    position: absolute; left: 56px; bottom: 86px;
    list-style: none;
    color: var(--ink-soft);
    font-weight: 400; font-size: 12px; line-height: 17px;
  }
  .contact li { display: flex; align-items: flex-start; gap: 10px; margin-bottom: 5px; }
  .contact svg { flex: none; width: 14px; height: 14px; margin-top: 2px; }
  .rule {
    position: absolute; left: 0; right: 0; bottom: 52px;
    height: 2px; background: var(--band);
  }
  .band {
    position: absolute; left: 0; right: 0; bottom: 0;
    height: 34px; background: var(--band);
  }
</style>
</head>
<body>
  <main class="letterhead">
    <header class="masthead">
      <div class="firm-name">
        <span>Ferraz</span>
        <span>Lacerda</span>
        <span>Moura</span>
        <span>Advogados</span>
      </div>
      <div class="brand-mark"><i></i>FLM</div>
    </header>

    <div class="ghost-name" aria-hidden="true">FLM</div>

    <ul class="contact">
      <li>
        <svg viewBox="0 0 14 14"><circle cx="7" cy="7" r="7" fill="var(--brand-light)"/><path d="M4.6 3.6l1.3 1.3-.7.9c.5 1 1.2 1.8 2.2 2.3l.9-.7 1.3 1.3-.8 1c-2.4-.4-4.5-2.5-5-5z" fill="#fff"/></svg>
        <span>(21) 3456-7890</span>
      </li>
      <li>
        <svg viewBox="0 0 14 14"><circle cx="7" cy="7" r="7" fill="var(--brand-light)"/><path d="M7 3a2.4 2.4 0 0 0-2.4 2.4C4.6 7.3 7 10.5 7 10.5s2.4-3.2 2.4-5.1A2.4 2.4 0 0 0 7 3zm0 3.3a.9.9 0 1 1 0-1.8.9.9 0 0 1 0 1.8z" fill="#fff"/></svg>
        <span>Rua das Acácias 210, 8º andar<br>Lagoa - Rio de Janeiro - RJ<br>CEP: 22470-010</span>
      </li>
      <li>
        <svg viewBox="0 0 14 14"><circle cx="7" cy="7" r="7" fill="var(--brand-light)"/><circle cx="7" cy="7" r="3.6" fill="none" stroke="#fff" stroke-width="1"/><path d="M3.4 7h7.2M7 3.4c-1.4 2-1.4 5.2 0 7.2M7 3.4c1.4 2 1.4 5.2 0 7.2" fill="none" stroke="#fff" stroke-width=".8"/></svg>
        <span>flmadv.com.br</span>
      </li>
    </ul>

    <div class="rule"></div>
    <div class="band"></div>
  </main>
</body>
</html>
```